Brivane - Business Cards for a new venture

create business card for a startup classified business dealing in construction materials, the cards need to have a professional look but modern, more serious than playful, one of the samples must include the official font (attached), please explore using the official colors in the company's logo

Target Market(s)

Energy sector

Contact Information for Business Card

Font styles to use
Other font styles liked:
• suissnord

Requirements
Must have
• corporate colors (in logo attached)
Nice to have
• Official font (in one of the samples) font is : suissnord
Should not have
• Cartoonish look

```html
<!DOCTYPE html>
<html lang="en">
<head>
<meta charset="utf-8">
<title>Brivane – Business Cards</title>
<link rel="stylesheet" href="https://fonts.googleapis.com/css2?family=Michroma&family=Montserrat:wght@500;600&display=swap">
<style>
  :root {
    --brand-blue: #0e4275;
    --card-white: #ffffff;
    --mark-grey: #8c8c8c;
    --page-bg: #e9e6e2;
  }
  * { margin: 0; padding: 0; box-sizing: border-box; }
  html, body {
    width: 1200px; height: 1189px; overflow: hidden;
    background: var(--page-bg);
  }
  .canvas { position: relative; width: 1200px; height: 1189px; }

  .card {
    position: absolute;
    background: var(--card-white);
    box-shadow: 0 14px 24px rgba(0,0,0,0.12);
  }

  /* Front */
  .card-front { left: 226px; top: 148px; width: 757px; height: 421px; padding: 14px; }
  .card-front .face {
    width: 100%; height: 100%;
    background: var(--brand-blue);
    display: flex; align-items: center; justify-content: center;
  }
  .wordmark {
    display: flex; align-items: center; gap: 18px;
    font-family: "Michroma", sans-serif;
    letter-spacing: 4px;
  }
  .wordmark-dot { width: 22px; height: 22px; border-radius: 50%; }
  .card-front .wordmark { color: var(--card-white); font-size: 34px; }
  .card-front .wordmark-dot { background: var(--card-white); }

  /* Back */
  .card-back { left: 230px; top: 627px; width: 751px; height: 419px; padding: 19px; }
  .card-back .frame {
    position: relative; width: 100%; height: 100%;
    background: var(--brand-blue);
  }
  .card-back .panel {
    position: absolute; left: 62px; top: 17px; right: 16px; bottom: 17px;
    background: var(--card-white);
  }
  .card-back .wordmark {
    position: absolute; left: 0; right: 0; top: 132px;
    justify-content: center;
    color: var(--mark-grey); font-size: 24px;
  }
  .card-back .wordmark-dot { background: var(--brand-blue); width: 18px; height: 18px; }

  .contact-list {
    position: absolute; left: 20px; top: 236px;
    list-style: none;
    font-family: "Montserrat", sans-serif; font-weight: 600;
    font-size: 16px; color: var(--brand-blue);
  }
  .contact-list li { display: flex; align-items: center; height: 31px; }
  .contact-icon { width: 20px; height: 20px; margin-right: 33px; flex: none; }
  .contact-icon * { fill: none; stroke: var(--card-white); stroke-width: 1.6; stroke-linecap: round; stroke-linejoin: round; }
  .phone-sep { margin: 0 16px; }
</style>
</head>
<body>
<main class="canvas">

  <section class="card card-front" aria-label="Business card front">
    <div class="face">
      <div class="wordmark"><span class="wordmark-dot"></span>BRIVANE</div>
    </div>
  </section>

  <section class="card card-back" aria-label="Business card back">
    <div class="frame">
      <div class="panel">
        <div class="wordmark"><span class="wordmark-dot"></span>BRIVANE</div>
      </div>
      <ul class="contact-list">
        <li>
          <svg class="contact-icon" viewBox="0 0 20 20"><rect x="2" y="4.5" width="16" height="11" rx="1"/><path d="M2.5 5 10 11 17.5 5"/></svg>
          <span>office@brivane-mail.com</span>
        </li>
        <li>
          <svg class="contact-icon" viewBox="0 0 20 20"><path d="M5 2.5 8 5.5 6.5 8a10 10 0 0 0 5.5 5.5L14.5 12l3 3-2 2.5C9 17 3 11 2.5 4.5Z"/></svg>
          <span>+995500417263</span><span class="phone-sep">/</span><span>+995500417263</span>
        </li>
        <li>
          <svg class="contact-icon" viewBox="0 0 20 20"><path d="M10 18s-5.5-6-5.5-10a5.5 5.5 0 0 1 11 0c0 4-5.5 10-5.5 10Z"/><circle cx="10" cy="8" r="2"/></svg>
          <span>Kilnway Street, Leeds</span>
        </li>
        <li>
          <svg class="contact-icon" viewBox="0 0 20 20"><circle cx="10" cy="10" r="8"/><path d="M2 10h16M10 2c-3 3-3 13 0 16M10 2c3 3 3 13 0 16"/></svg>
          <span>www.brivane-build.com</span>
        </li>
      </ul>
    </div>
  </section>

</main>
</body>
</html>
```